Electrical Contractor's Business Stationary

I need a custom designed Stationery set for my Electrical Contracting business.

My trading business name is "BLUEPINE ELECTRICAL" please use this name and the attached vektor file of my trademarked logo

I have a (Sketch Harbor) designed logo & font style I have trademarked, and would like that used in the Stationary.

I need to be able to write to clients with letterhead's and footers, so my business can display that we are a professional team.

Please stick with the colours of "Green/Red/Black" as in my logo, on white backgrounds

Target Market(s)

Commercial clients/customers

Residential clients/customers

Industrial clients/customers

Home owners

Business owners

Holiday home owners

Investors

First home buyers

Industry/Entity Type

Business

Requirements
Must have
• Must be in A4 format

My trademarked logo (file uploaded & can you add a very small "TM" at the end)

my WOPT group membership logo (which I have also included)

My Electrical Contractor License No,
My ABN (Australian Business Number),
My email address,
My Website address,

my mobile phone - fax - office phone numbers
(As per screenshot of a sample invoice which is attached, and these details can be strung out along the bottom footer or wherever, as I'm looking for inventiveness )

And the areas my business covers " SYDNEY - CENTRAL COAST - NEWCASTLE", somewhere on the stationary also.

Thanks guys!!

```html
<!DOCTYPE html>
<html lang="en">
<head>
<meta charset="utf-8">
<title>Bluepine Electrical — Stationery Set</title>
<link href="https://fonts.googleapis.com/css2?family=Open+Sans:wght@400;600;700&family=Great+Vibes&display=swap" rel="stylesheet">
<style>
  :root {
    --bg: #ebebeb;
    --paper: #ffffff;
    --brand-red: #b8252f;
    --brand-green: #8cbf3f;
    --ink: #4a4a4a;
    --ink-dark: #2e2e2e;
    --ink-soft: #8a8a8a;
    --badge: #2c4a8c;
  }
  * { box-sizing: border-box; margin: 0; padding: 0; }
  html, body { width: 1200px; height: 800px; overflow: hidden; }
  body {
    background: var(--bg);
    font-family: "Open Sans", Arial, sans-serif;
    color: var(--ink);
    position: relative;
  }

  /* Business name */
  .brand-name {
    position: absolute;
    font-weight: 600;
    color: var(--ink-dark);
    line-height: 1;
    white-space: nowrap;
  }

  /* Letterhead (A4) */
  .letterhead {
    position: absolute; left: 235px; top: 40px;
    width: 509px; height: 720px;
    background: var(--paper);
    box-shadow: 0 2px 8px rgba(0,0,0,.12);
  }
  .letterhead .brand-name { left: 37px; top: 52px; font-size: 18px; }

  .service-areas {
    position: absolute; right: 37px; top: 72px;
    font-size: 7.5px; color: var(--brand-red); font-weight: 600;
    white-space: nowrap;
  }

  .letter-body {
    position: absolute; left: 62px; top: 196px; width: 420px;
    font-size: 9.4px; line-height: 13.6px; color: var(--ink);
  }
  .salutation { font-weight: 700; margin-bottom: 14px; }
  .letter-body p { margin-bottom: 13.6px; }

  .sign-off { position: absolute; left: 62px; top: 582px; }
  .signature { font-family: "Great Vibes", cursive; font-size: 26px; color: var(--ink-dark); line-height: 1; word-spacing: 4px; }
  .sign-role { font-size: 9.5px; font-weight: 700; color: var(--ink-soft); margin-top: 0; }

  .letter-footer {
    position: absolute; left: 37px; right: 37px; top: 673px;
    display: flex; justify-content: space-between; align-items: center;
  }
  .footer-details {
    border-left: 4px solid var(--brand-red);
    padding-left: 8px;
    font-size: 6.6px; line-height: 9.6px; color: var(--ink-dark);
  }
  .footer-details .key { color: var(--brand-red); }
  .footer-details .web { color: var(--brand-red); font-weight: 700; }
  .member-badge { width: 40px; height: 12px; background: var(--badge); border-radius: 2px; }

  /* Business cards */
  .card {
    position: absolute; width: 232px; height: 128px;
    background: var(--paper);
    box-shadow: 0 2px 6px rgba(0,0,0,.12);
  }
  .card-front { left: 900px; top: 436px; }
  .card-front .brand-name { right: 18px; top: 52px; font-size: 12px; }
  .card-front .service-areas { right: 18px; top: 70px; font-size: 5px; }

  .card-back { left: 900px; top: 618px; }
  .card-back .brand-name { left: 14px; top: 22px; font-size: 10px; }
  .card-holder { position: absolute; left: 50px; top: 56px; font-size: 8px; color: var(--ink-dark); white-space: nowrap; }
  .card-holder span { font-size: 5px; margin-left: 3px; }
  .card-contacts {
    position: absolute; left: 50px; top: 72px;
    border-left: 1.5px solid var(--brand-red); padding-left: 5px;
    font-size: 5px; line-height: 8px; color: var(--ink-dark);
  }
  .card-contacts .key { color: var(--brand-red); }
  .card-contacts .web { color: var(--brand-red); font-weight: 700; }
</style>
</head>
<body>

<section class="letterhead">
  <div class="brand-name">BLUEPINE ELECTRICAL</div>
  <div class="service-areas">SYDNEY - CENTRAL COAST - NEWCASTLE</div>

  <div class="letter-body">
    <p class="salutation">Lorem Ipsum,</p>
    <p>Cras mattis consectetur purus sit amet fermentum. Etiam porta sem malesuada magna mollis euismod. Integer posuere erat a ante venenatis dapibus posuere velit aliquet. Cras justo odio, dapibus ac facilisis in, egestas eget quam. Aenean eu leo quam. Pellentesque ornare sem lacinia quam venenatis vestibulum.</p>
    <p>Vivamus sagittis lacus vel augue laoreet rutrum faucibus dolor auctor. Donec sed odio dui. Etiam porta sem malesuada magna mollis euismod. Morbi leo risus, porta ac consectetur ac, vestibulum at eros. Nullam id dolor id nibh ultricies vehicula ut id elit.</p>
    <p>Donec id elit non mi porta gravida at eget metus. Fusce dapibus, tellus ac cursus commodo, tortor mauris condimentum nibh, ut fermentum massa justo sit amet risus. Cras justo odio, dapibus ac facilisis in, egestas eget quam. Cum sociis natoque penatibus et magnis dis parturient montes, nascetur ridiculus mus.</p>
    <p>Cum sociis natoque penatibus et magnis dis parturient montes, nascetur ridiculus mus. Curabitur blandit tempus porttitor. Aenean lacinia bibendum nulla sed consectetur. Lorem ipsum dolor sit amet, consectetur adipiscing elit.</p>
    <p>Cras justo odio, dapibus ac facilisis in, egestas eget quam. Morbi leo risus, porta ac consectetur ac, vestibulum at eros. Duis mollis, est non commodo luctus, nisi erat porttitor ligula, eget lacinia odio sem nec elit. Integer posuere erat a ante venenatis dapibus posuere velit aliquet. Vivamus sagittis lacus vel augue laoreet rutrum faucibus dolor auctor.</p>
  </div>

  <div class="sign-off">
    <div class="signature">Your Name</div>
    <div class="sign-role">Company Director</div>
  </div>

  <footer class="letter-footer">
    <div class="footer-details">
      Licensed Electrical Contractor | Lic No. 555018c | ABN: 00 555 123 456<br>
      <span class="key">T</span> (02) 5550 1184 | <span class="key">M</span> 0400 555 219 | <span class="key">F</span> (02) 5550 1190<br>
      <span class="key">E</span> accounts@bluepineelectrical.com.au | <span class="web">www.bluepineelectrical.com.au</span>
    </div>
    <div class="member-badge" role="img" aria-label="WOPT group membership badge"></div>
  </footer>
</section>

<section class="card card-front">
  <div class="brand-name">BLUEPINE ELECTRICAL</div>
  <div class="service-areas">SYDNEY - CENTRAL COAST - NEWCASTLE</div>
</section>

<section class="card card-back">
  <div class="brand-name">BLUEPINE ELECTRICAL</div>
  <div class="card-holder">MIRA STENHOLT<span>Principal designer</span></div>
  <div class="card-contacts">
    <span class="key">T</span> (02) 5550 1184<br>
    <span class="key">M</span> 0400 555 219<br>
    <span class="key">F</span> (02) 5550 1190<br>
    <span class="key">E</span> accounts@bluepineelectrical.com.au<br>
    <span class="web">www.bluepineelectrical.com.au</span>
  </div>
</section>

</body>
</html>
```